Business Cards that are elegant and wow

I want to create and print business cards that represent my brand and stand out from the rest. We want to ensure they stay in our branding and the integrity is not lost. I am happy to look at different shapes like square etc.

It will be printed on very thick cards and will be stylish .

I want to create and print business cards that represent my brand and stand out from the rest. We want to ensure they stay in ur branding and the integrity is not lost. I am happy to look at different shapes like square etc.

Target Market(s)

real estate professionals

Industry/Entity Type

Real Estate

Contact Information for Business Card

Maren Holt
hello@brightfernrealty.com.au
brightfernrealty.com.au
0487 316 252 (SMS)

Colors

Designer to choose colors to be used in the design.

Requirements
Must have
• My logo
• email
• website
• Name
Nice to have
• I like the idea of printing with foil or spot gloss. You want it to stand out in a sea.
Should not have
• I would like you to stay in my colour themes. Don't change the colour of my logo

```html
<!DOCTYPE html>
<html lang="en">
<head>
<meta charset="utf-8">
<title>Bright Fern Realty — Business Card</title>
<link href="https://fonts.googleapis.com/css2?family=Montserrat:wght@400;500;700&display=swap" rel="stylesheet">
<style>
  :root {
    --backdrop: #2a2a2c;
    --card: #141415;
    --card-edge: #1e1e20;
    --foil: #d6d6d8;
    --brand-pink: #c2185b;
    --brand-blue: #1e9bd7;
    --contact-text: #cfd1d4;
  }
  * { margin: 0; padding: 0; box-sizing: border-box; }
  html, body {
    width: 1200px;
    height: 1017px;
    overflow: hidden;
    background: var(--backdrop);
    font-family: "Montserrat", sans-serif;
  }
  .sheet {
    position: relative;
    width: 1200px;
    height: 1017px;
  }
  .card {
    position: absolute;
    width: 520px;
    height: 300px;
    background: var(--card);
    border: 1px solid var(--card-edge);
    border-radius: 4px;
    box-shadow: 0 24px 50px rgba(0,0,0,0.45);
  }
  .card--front { left: 70px; top: 170px; }
  .card--back  { left: 610px; top: 540px; }

  /* Front: foil wordmark */
  .front-mark {
    position: absolute;
    left: 50%;
    top: 50%;
    transform: translate(-50%, -50%);
    display: flex;
    align-items: center;
    gap: 16px;
    white-space: nowrap;
  }
  .front-mark__dot {
    width: 50px;
    height: 50px;
    border: 2px solid var(--foil);
    border-radius: 50%;
  }
  .front-mark__name {
    color: var(--foil);
    font-size: 24px;
    font-weight: 500;
    letter-spacing: 3px;
    text-transform: uppercase;
  }

  /* Back: brand + contact */
  .back-mark {
    position: absolute;
    right: 34px;
    top: 34px;
    display: flex;
    align-items: center;
    gap: 10px;
  }
  .back-mark__dot {
    width: 30px;
    height: 30px;
    border: 3px solid var(--brand-pink);
    border-radius: 50%;
  }
  .back-mark__name {
    color: var(--brand-blue);
    font-size: 14px;
    font-weight: 700;
    letter-spacing: 1.5px;
    text-transform: uppercase;
  }
  .contact {
    position: absolute;
    left: 40px;
    bottom: 36px;
    list-style: none;
  }
  .contact__row {
    display: flex;
    align-items: center;
    gap: 14px;
    height: 28px;
    color: var(--contact-text);
    font-size: 13px;
    font-weight: 400;
  }
  .contact__row--name {
    color: var(--brand-blue);
    font-size: 17px;
    font-weight: 700;
    letter-spacing: 1px;
    text-transform: uppercase;
    margin-bottom: 6px;
  }
  .contact__icon {
    width: 18px;
    height: 18px;
    flex: none;
  }
</style>
</head>
<body>
<main class="sheet">

  <section class="card card--front" aria-label="Card front">
    <div class="front-mark">
      <span class="front-mark__dot"></span>
      <span class="front-mark__name">Bright Fern Realty</span>
    </div>
  </section>

  <section class="card card--back" aria-label="Card back">
    <div class="back-mark">
      <span class="back-mark__dot"></span>
      <span class="back-mark__name">Bright Fern Realty</span>
    </div>

    <ul class="contact">
      <li class="contact__row contact__row--name">
        <svg class="contact__icon" viewBox="0 0 18 18" aria-hidden="true">
          <circle cx="9" cy="9" r="8" fill="none" stroke="var(--brand-pink)" stroke-width="1.4"/>
          <circle cx="9" cy="7" r="2.4" fill="var(--brand-blue)"/>
          <path d="M4.8 13.4c.8-2.2 2.3-3.2 4.2-3.2s3.4 1 4.2 3.2z" fill="var(--brand-blue)"/>
        </svg>
        Maren Holt
      </li>
      <li class="contact__row">
        <svg class="contact__icon" viewBox="0 0 18 18" aria-hidden="true">
          <circle cx="9" cy="9" r="8" fill="none" stroke="var(--brand-pink)" stroke-width="1.4"/>
          <path d="M6.2 5.2l1.6-.4 1 2.2-1 .8c.5 1.1 1.3 1.9 2.4 2.4l.8-1 2.2 1-.4 1.6c-3.6.2-6.8-3-6.6-6.6z" fill="var(--brand-blue)"/>
        </svg>
        0487 316 252
      </li>
      <li class="contact__row">
        <svg class="contact__icon" viewBox="0 0 18 18" aria-hidden="true">
          <circle cx="9" cy="9" r="8" fill="none" stroke="var(--brand-pink)" stroke-width="1.4"/>
          <rect x="5" y="6" width="8" height="6" rx="0.6" fill="var(--brand-blue)"/>
          <path d="M5.3 6.4L9 9.3l3.7-2.9" fill="none" stroke="var(--card)" stroke-width="0.9"/>
        </svg>
        hello@brightfernrealty.com.au
      </li>
      <li class="contact__row">
        <svg class="contact__icon" viewBox="0 0 18 18" aria-hidden="true">
          <circle cx="9" cy="9" r="8" fill="none" stroke="var(--brand-pink)" stroke-width="1.4"/>
          <circle cx="9" cy="9" r="4" fill="none" stroke="var(--brand-blue)" stroke-width="1.1"/>
          <ellipse cx="9" cy="9" rx="1.7" ry="4" fill="none" stroke="var(--brand-blue)" stroke-width="1"/>
          <path d="M5 9h8" stroke="var(--brand-blue)" stroke-width="1"/>
        </svg>
        www.brightfernrealty.com.au
      </li>
    </ul>
  </section>

</main>
</body>
</html>
```